Martial Arts School needs a Trial Pass for new members

Looking for something that I can give to someone to come try a class at my martial arts school. We primarily offer two class types; kickboxing and jiu jitsu. Im looking for some type of dual discipline free trial pass to give to people at local businesses or events. I want it to look clean and sharp more over I want to create a feeling of great value and quality check out my website for guidance www.ironcrestdojo.com

Target Market(s)

Most of my students are anywhere from 15-16 all the way up to 35 for the most part. Young adults who are into martial arts and fitness

Industry/Entity Type

Martial Art

Colors
0255a3
000000
fbed22

Requirements
Must have
• I would like to include my logos and I would like for what is going on in the flyer to match what is going on in the school. I don't want people seeing one thing and coming in to try a class and seeing another
Nice to have
• if anyone needs different types of files to get my logos right just let me know I can get whatever to you check out the website to get a look and feel for our school
• www.ironcrestdojo.com
Should not have
• Any pictures of people in a karate outfit or gi we dont wear them

```html
<!DOCTYPE html>
<html lang="en">
<head>
<meta charset="utf-8">
<title>Ironcrest Free Trial Pass – Kickboxing &amp; Jiu-Jitsu</title>
<link rel="stylesheet" href="https://fonts.googleapis.com/css2?family=Anton&family=Roboto+Condensed:wght@400;700&display=swap">
<style>
  :root{
    --yellow:#fbed22;
    --blue:#0255a3;
    --black:#000000;
    --ink:#1a1a1a;
    --grey:#444444;
    --white:#ffffff;
    --photo-dark:#121212;
    --photo-skin:#9a7a66;
    --photo-warm:#5a4638;
  }
  *{margin:0;padding:0;box-sizing:border-box}
  html,body{width:1200px;height:3196px;overflow:hidden;background:var(--white)}
  .pass{position:relative;width:1200px;height:3196px;overflow:hidden;font-family:"Roboto Condensed",Arial,sans-serif}

  .hero{position:absolute;left:0;top:0;width:1200px;height:1360px;
    background:
      radial-gradient(ellipse 420px 520px at 62% 44%,var(--photo-skin) 0%,var(--photo-warm) 45%,rgba(18,18,18,0) 100%),
      radial-gradient(ellipse 360px 300px at 28% 40%,#6e564a 0%,rgba(18,18,18,0) 100%),
      linear-gradient(180deg,#1c1c1c 0%,#262626 55%,var(--photo-dark) 100%)}
  .hero-title{position:absolute;left:0;top:70px;width:1200px;text-align:center;
    font-family:"Anton",Impact,sans-serif;color:var(--yellow);text-transform:uppercase;letter-spacing:2px}
  .hero-title .line-main{display:block;font-size:150px;line-height:150px}
  .hero-title .line-disc{display:block;font-size:112px;line-height:130px}
  .blue-band{position:absolute;left:0;top:1360px;width:1200px;height:34px;background:var(--blue)}

  .offer{position:absolute;left:0;top:1394px;width:1200px;height:1226px;background:var(--white)}
  .offer-title{position:absolute;left:0;top:40px;width:1200px;text-align:center;
    font-weight:700;font-size:96px;line-height:104px;color:var(--ink)}
  .offer-sub{position:absolute;left:0;top:262px;width:1200px;text-align:center;
    font-size:54px;line-height:64px;color:var(--ink)}
  .benefits{position:absolute;left:150px;top:420px;list-style:none}
  .benefits li{position:relative;padding-left:56px;font-size:50px;line-height:88px;color:var(--grey)}
  .benefits svg{position:absolute;left:0;top:24px;width:40px;height:40px}
  .cta{position:absolute;left:60px;top:990px;width:470px;font-size:46px;line-height:58px;color:var(--ink)}
  .partner{position:absolute;left:640px;top:1010px;display:flex;align-items:center;gap:22px}
  .partner-dot{width:64px;height:64px;border-radius:50%;background:var(--yellow)}
  .partner-name{font-weight:700;font-size:110px;line-height:1;color:var(--yellow)}

  .footer{position:absolute;left:0;top:2620px;width:1200px;height:576px;background:var(--black)}
  .social{position:absolute;right:90px;top:46px;display:flex;gap:14px}
  .social span{width:50px;height:50px;border-radius:50%;background:var(--grey)}
  .brand{position:absolute;left:0;top:110px;width:1200px;text-align:center;color:var(--white)}
  .brand-name{font-weight:700;font-size:150px;line-height:150px}
  .brand-tag{font-size:44px;line-height:50px;letter-spacing:2px}
  .contact{position:absolute;left:0;top:430px;width:1200px;text-align:center;
    font-weight:700;font-size:66px;line-height:80px;color:var(--white)}
</style>
</head>
<body>
<main class="pass">
  <section class="hero" role="img" aria-label="Photo of a fighter in striped shorts throwing a punch under dark arena lighting">
    <h1 class="hero-title"><span class="line-main">Free Trial Pass</span><span class="line-disc">Kickboxing &amp; Jiu-Jitsu</span></h1>
  </section>
  <div class="blue-band"></div>

  <section class="offer">
    <h2 class="offer-title">Lehigh Valley<br>Kickboxing &amp; Jiu-Jitsu</h2>
    <p class="offer-sub">Action Packed 800 Calorie Kickboxing<br>Workout in Lehigh Valley</p>
    <ul class="benefits">
      <li><svg viewBox="0 0 40 40"><path d="M4 22 L15 33 L36 6" fill="none" stroke="#fbed22" stroke-width="6" stroke-linecap="round" stroke-linejoin="round"/></svg>Increase your self-confidence</li>
      <li><svg viewBox="0 0 40 40"><path d="M4 22 L15 33 L36 6" fill="none" stroke="#fbed22" stroke-width="6" stroke-linecap="round" stroke-linejoin="round"/></svg>Serious energy upgrades!</li>
      <li><svg viewBox="0 0 40 40"><path d="M4 22 L15 33 L36 6" fill="none" stroke="#fbed22" stroke-width="6" stroke-linecap="round" stroke-linejoin="round"/></svg>Drastic reduction in stress levels</li>
      <li><svg viewBox="0 0 40 40"><path d="M4 22 L15 33 L36 6" fill="none" stroke="#fbed22" stroke-width="6" stroke-linecap="round" stroke-linejoin="round"/></svg>Gain razor-sharp concentration skills</li>
      <li><svg viewBox="0 0 40 40"><path d="M4 22 L15 33 L36 6" fill="none" stroke="#fbed22" stroke-width="6" stroke-linecap="round" stroke-linejoin="round"/></svg>Your fitness levels will be off the chart</li>
      <li><svg viewBox="0 0 40 40"><path d="M4 22 L15 33 L36 6" fill="none" stroke="#fbed22" stroke-width="6" stroke-linecap="round" stroke-linejoin="round"/></svg>Effortless weight maintenance</li>
    </ul>
    <p class="cta">Take advantage of this great offer. Call for details. A $50 value.</p>
    <div class="partner">
      <span class="partner-name">Vantor</span>
      <span class="partner-dot"></span>
    </div>
  </section>

  <footer class="footer">
    <div class="social"><span></span><span></span><span></span><span></span></div>
    <div class="brand">
      <div class="brand-name">Ironcrest</div>
      <div class="brand-tag">MMA-Jiu-Jitsu<br>Kickboxing</div>
    </div>
    <p class="contact">ironcrestdojo.com • 555.014.2290</p>
  </footer>
</main>
</body>
</html>
```